Cellular Repair Retail Store Flyer/Postcards

We are looking for a good flyer for us to print and distribute as well as post on various web sites. Our company name is "Handset Fixit Crew" and we repair a wide range of cellular phones from Zelphones to Zelpads, Varnok's,,QT's, Brivanta, and PWD. In general if you have a cell phone we repair it. Cellular repairs is the primary focus however we are also an accessory superstore with 1'000's of choices of phone cases for all model phones. Historically these phone cases have all been aftermarket however now there are a number of brands. I'll attach a few so we have the ability to use some branded logo's on the flyer. Not all the graphics need to be used that we are providing. Again the flyer's main objective is, 1) Cellular Repairs, 2) Our location & pic of building (I have one attached but i'll have a new one within 24 hours and 3) Cellular Accessory Superstore with 1,000's of case. The address to our location is 4817 N 19th Street, Milwaukee, Wisconsin 53209. Anytime we use our address we state "2 Blocks North of 19th & Pemberly" (popular intersection in the market). So i'm not sure what approach to go... but I figured i'd provide a bunch of stuff for you to pick from. Naturally let's not make the flyer too busy but if we hit the 3 main deal points we will be good. Attached are; some pics of attractive phone cases, a few cellular accessory brands such as Heron Shell, Valdoro, Skinmitten, LuVenn, Cragmore etc. These logo's may add a nice appeal given they are national companies. For your reference and to be listed on the flyer is our web site; www.handsetfixitcrew.example

Requirements
Must have
• This advertisement will be used for the Postal Porchdrop Bulk Mailer so we need to make the flyer with the following measurements in mind; 6.25" x 9"
Nice to have
• In addition to repairing phones we need to promote we buy used and broken smart phones. Repairs done on site with certified technicians.

```html
<!DOCTYPE html>
<html lang="en">
<head>
<meta charset="utf-8">
<title>Handset Fixit Crew – Repair Flyer</title>
<link rel="stylesheet" href="https://fonts.googleapis.com/css2?family=Questrial&display=swap">
<style>
  :root {
    --blue: #1e8fc6;
    --teal: #2aa3b8;
    --teal-light: #5fc3cf;
    --dark: #3a3d42;
    --dark-deep: #26282c;
    --ink: #2d2f33;
    --white: #ffffff;
    --paper: #f7f7f5;
  }
  html, body {
    margin: 0;
    width: 833px;
    height: 1200px;
    overflow: hidden;
    background: var(--paper);
  }
  .flyer {
    position: relative;
    width: 833px;
    height: 1200px;
    background: var(--white);
    font-family: "Questrial", "Century Gothic", sans-serif;
    color: var(--ink);
    overflow: hidden;
  }
  .backdrop { position: absolute; inset: 0; }
  .brand-name {
    position: absolute; left: 60px; top: 50px; margin: 0;
    font-size: 36px; font-weight: 400; color: var(--blue);
    display: flex; align-items: center; gap: 12px;
  }
  .brand-name .mark { width: 14px; height: 14px; background: var(--blue); }
  .site-url {
    position: absolute; left: 562px; top: 192px;
    font-size: 18px; line-height: 22px; color: var(--white);
    white-space: nowrap;
    transform: rotate(-29deg); transform-origin: left top;
    letter-spacing: 0.5px;
  }
  .headline {
    position: absolute; left: 60px; top: 180px; margin: 0;
    font-size: 40px; font-weight: 400; line-height: 1.2; color: var(--ink);
  }
  .headline .accent { color: var(--blue); }
  .phones-photo {
    position: absolute; left: 520px; top: 260px; width: 280px; height: 250px;
    background: linear-gradient(135deg, #d9e3ea, #8a97a3 55%, #2e3339);
    border-radius: 6px;
  }
  .repairs-title {
    position: absolute; left: 180px; top: 440px; margin: 0;
    font-size: 42px; font-weight: 400; color: var(--white);
  }
  .building-photo {
    position: absolute; left: 60px; top: 540px; width: 220px; height: 200px;
    background: linear-gradient(160deg, #c9d6df, #7d8c97 60%, #4a545c);
  }
  .address {
    position: absolute; left: 310px; top: 565px; width: 270px;
    font-size: 19px; line-height: 1.3; color: var(--white);
    display: flex; gap: 10px;
  }
  .address svg { flex: none; margin-top: 3px; }
  .call-out {
    position: absolute; left: 600px; top: 610px;
    font-size: 20px; line-height: 1.3; color: var(--white);
  }
  .call-out .accent { color: var(--teal-light); }
  .accessory-title {
    position: absolute; left: 420px; top: 745px; margin: 0;
    font-size: 40px; font-weight: 400; color: var(--blue);
  }
  .partner-row {
    position: absolute; left: 60px; top: 765px; width: 340px;
    display: flex; gap: 12px; font-size: 12px; color: var(--dark-deep);
    align-items: center;
  }
  .partner-row span { display: flex; align-items: center; gap: 5px; }
  .partner-row i { width: 8px; height: 8px; background: var(--dark-deep); display: inline-block; }
  .accessory-copy {
    position: absolute; left: 60px; top: 800px; width: 345px; margin: 0;
    font-size: 15px; line-height: 1.4; color: var(--ink);
  }
  .cases-photo {
    position: absolute; left: 430px; top: 800px; width: 370px; height: 210px;
    background: linear-gradient(90deg, #e85a8a, #f3c34a 30%, #5ab6d9 60%, #8a5bc4);
    opacity: 0.85;
  }
  .buy-line {
    position: absolute; left: 60px; top: 1000px; margin: 0;
    font-size: 30px; font-weight: 400; line-height: 1.15; color: var(--ink);
  }
  .tech-line {
    position: absolute; left: 60px; top: 1090px; margin: 0;
    font-size: 23px; color: var(--ink);
  }
  .tech-line .accent { color: var(--teal); }
</style>
</head>
<body>
<main class="flyer">
  <svg class="backdrop" width="833" height="1200" viewBox="0 0 833 1200" aria-hidden="true">
    <polygon points="260,360 833,40 833,118 400,360" fill="var(--dark)"/>
    <polygon points="0,380 833,300 833,480 0,570" fill="var(--teal)"/>
    <polygon points="0,570 833,480 833,510 0,600" fill="var(--dark)"/>
    <polygon points="0,600 833,510 833,730 0,730" fill="var(--dark-deep)"/>
  </svg>

  <h1 class="brand-name"><span class="mark"></span>Handset Fixit Crew</h1>
  <div class="site-url">www.handsetfixitcrew.example</div>

  <h2 class="headline">Bring Your <span class="accent">Broken</span> or<br>Damaged<br>Phone</h2>

  <div class="phones-photo" role="img" aria-label="Photo of two smartphones with cracked screens"></div>

  <h2 class="repairs-title">Cellular Repairs</h2>

  <div class="building-photo" role="img" aria-label="Photo of the store building front"></div>

  <div class="address">
    <svg width="18" height="26" viewBox="0 0 18 26"><path d="M9 0a9 9 0 0 0-9 9c0 7 9 17 9 17s9-10 9-17a9 9 0 0 0-9-9z" fill="#fff"/><circle cx="9" cy="9" r="3.5" fill="var(--dark-deep)"/></svg>
    <span>4817 N 19th Street, Milwaukee, Wisconsin 53209, 2 Blocks North of 19th &amp; Pemberly</span>
  </div>

  <div class="call-out">Get <span class="accent">Your Phone</span><br><span class="accent">Fixed</span> Today<br>414 - 555 - 0193</div>

  <h2 class="accessory-title">Cellular Accessory</h2>

  <div class="partner-row">
    <span><i></i>Valdoro</span>
    <span><i></i>Heron Shell</span>
    <span><i></i>Cragmore</span>
    <span><i></i>Skinmitten</span>
  </div>

  <p class="accessory-copy">Handset Fixit Crew also provides it's customers with a wide selection of phone accessories and Bluetooth devices that will allow your phone to stand out and be unique. We have accessories for every make and model. No matter what you have, you will be able to find something to stand out from the crowd.</p>

  <div class="cases-photo" role="img" aria-label="Photo of a wall display of colourful phone cases"></div>

  <p class="buy-line">we buy used and broken<br>smart phones</p>
  <p class="tech-line"><span class="accent">Professional On-Site</span> Technicians</p>
</main>
</body>
</html>
```